Brightwave Travel and Tours

Hotel Reservations
Airline Ticketing
Day Tour

My business is a Travel agency. My services are issuing domestic and international tickets. Book room/hotel reservations local/international.
My color preference is apple green/orange/red/blue.
Images of beaches, tickets,luggage.

```html
<!DOCTYPE html>
<html lang="en">
<head>
<meta charset="utf-8">
<title>Brightwave Travel and Tours – Business Card</title>
<link href="https://fonts.googleapis.com/css2?family=Source+Sans+3:ital,wght@0,400;0,600;1,400&display=swap" rel="stylesheet">
<style>
  :root {
    --bg: #3b3b3b;
    --card: #f7f7f7;
    --navy: #0f5f82;
    --teal: #166d92;
    --sky: #35b6e6;
    --ink: #333333;
    --muted: #4a4a4a;
    --orange: #f08a1c;
  }
  * { margin: 0; padding: 0; box-sizing: border-box; }
  html, body { width: 1200px; height: 750px; overflow: hidden; }
  body {
    background: var(--bg);
    font-family: "Source Sans 3", sans-serif;
    position: relative;
  }
  .card {
    position: absolute;
    top: 228px;
    width: 461px;
    height: 262px;
    background: var(--card);
    border-radius: 14px;
    overflow: hidden;
  }
  .card--front { left: 124px; }
  .card--back { left: 618px; }

  .front-band {
    position: absolute;
    left: 0; top: 0;
    width: 200px; height: 262px;
  }

  .contact {
    position: absolute;
    right: 27px; top: 22px;
    text-align: right;
  }
  .contact__name {
    color: var(--teal);
    font-weight: 600;
    font-size: 18px;
    line-height: 1.2;
  }
  .contact__role {
    color: var(--ink);
    font-size: 13px;
    line-height: 1.2;
    margin-bottom: 12px;
  }
  .contact__address {
    color: var(--muted);
    font-size: 11px;
    line-height: 16px;
    margin-right: 2px;
    margin-bottom: 2px;
  }
  .contact__line {
    display: flex;
    justify-content: flex-end;
    align-items: center;
    gap: 9px;
    color: var(--muted);
    font-size: 11px;
    line-height: 18.5px;
  }
  .contact__line svg { width: 13px; height: 13px; fill: var(--teal); }

  .wordmark {
    color: var(--teal);
    font-weight: 600;
    text-transform: uppercase;
    letter-spacing: 1px;
    line-height: 1;
  }
  .card--front .wordmark {
    position: absolute;
    right: 27px; bottom: 24px;
    text-align: right;
  }
  .wordmark__name { display: block; font-size: 27px; }
  .wordmark__sub { display: block; font-size: 13.5px; letter-spacing: 2px; margin-top: 1px; }

  .back-logo {
    position: absolute;
    left: 0; right: 0; top: 58px;
    display: flex;
    flex-direction: column;
    align-items: center;
  }
  .back-logo__circle {
    width: 62px; height: 62px;
    border-radius: 50%;
    background: var(--sky);
    margin-bottom: 14px;
  }
  .card--back .wordmark { text-align: center; }
  .card--back .wordmark__name { font-size: 26px; }
  .card--back .wordmark__sub { font-size: 13px; }

  .services {
    position: absolute;
    left: 0; right: 0; top: 212px;
    text-align: center;
    color: var(--teal);
    font-style: italic;
    font-size: 14px;
  }
  .services__dot { color: var(--orange); font-style: normal; margin: 0 4px; }
</style>
</head>
<body>

  <section class="card card--front">
    <svg class="front-band" viewBox="0 0 200 262" aria-hidden="true">
      <path d="M0 0 H100 C60 60 40 130 60 200 C70 230 90 250 105 262 H0 Z" fill="var(--navy)"/>
      <circle cx="128" cy="132" r="62" fill="var(--sky)"/>
    </svg>

    <div class="contact">
      <div class="contact__name">Daniel Reyes</div>
      <div class="contact__role">CEO/Founder</div>
      <div class="contact__address">214 Harbor View Road<br>Coral Bay, Florida 33901</div>
      <div class="contact__line">555 210 4836
        <svg viewBox="0 0 16 16"><path d="M3.5 1 6 4 4.8 5.8c.9 2 2.4 3.5 4.4 4.4L11 9l3 2.5-1.3 2.5C7 13.8 2.2 9 2 3.3Z"/></svg>
      </div>
      <div class="contact__line">555 318 7720
        <svg viewBox="0 0 16 16"><path d="M4.5 1h7a1 1 0 0 1 1 1v12a1 1 0 0 1-1 1h-7a1 1 0 0 1-1-1V2a1 1 0 0 1 1-1Zm.5 2v9h6V3Zm3 10a.8.8 0 1 0 0 .1Z"/></svg>
      </div>
      <div class="contact__line">555 402 6159
        <svg viewBox="0 0 16 16"><path d="M4 1h6l2 2v3H4Zm-2 6h12a1 1 0 0 1 1 1v5H1V8a1 1 0 0 1 1-1Zm2 7h8v1H4Z"/></svg>
      </div>
      <div class="contact__line">hello@brightwave.travel
        <svg viewBox="0 0 16 16"><path d="M1 3h14v10H1Zm1.2 1.2L8 8.6l5.8-4.4Z" fill-rule="evenodd"/></svg>
      </div>
      <div class="contact__line">www.brightwave.travel
        <svg viewBox="0 0 16 16"><circle cx="8" cy="8" r="7"/><path d="M1 8h14M8 1c-3 3-3 11 0 14M8 1c3 3 3 11 0 14" stroke="#fff" stroke-width="1" fill="none"/></svg>
      </div>
    </div>

    <div class="wordmark">
      <span class="wordmark__name">Brightwave</span>
      <span class="wordmark__sub">Travel and Tours</span>
    </div>
  </section>

  <section class="card card--back">
    <div class="back-logo">
      <div class="back-logo__circle"></div>
      <div class="wordmark">
        <span class="wordmark__name">Brightwave</span>
        <span class="wordmark__sub">Travel and Tours</span>
      </div>
    </div>
    <p class="services">Hotel Reservations<span class="services__dot">•</span>Airline Ticketing<span class="services__dot">•</span>Day Tour</p>
  </section>

</body>
</html>
```